Design a modern, premium front panel for a stand-up pouch

Design a modern, premium front for a stand-up pouch for VELUTRA. Product is for Urine/vomit/runny stool incidents indoors; quick cleanups before smell sets; nighttime/elderly pet accidents; travel/car mishaps.

It must instantly show it’s for dogs & cats and include three small step icons with labels: Sprinkle → Wait 1–5 min → Sweep. Front copy to include: VELUTRA, descriptor “Mineral Instant Absorber – for Dogs & Cats”, one benefits line “Fragrance-Free • 100 % Mineral • Odor-Binding • Low-Dust

Goal: clear who/what/how in under 3 seconds
Deliverables: AI/PDF + a pouch mockup;

Target Market(s)

• Dog & cat households in apartments/homes; new pet parents, senior pets, multi-pet homes. • Cleanliness & odor-sensitive buyers (allergies/asthma, fragrance-free preference). • Surfaces at risk: carpets/rugs, sofas, mattresses, car interiors.

Industry/Entity Type

Pet e-commerce and retail

Font styles to use
Other font styles liked:
• like attached images

Requirements
Nice to have
• light background, eco friendly

```html
<!DOCTYPE html>
<html lang="en">
<head>
<meta charset="utf-8">
<title>VELUTRA Mineral Instant Absorber – Pouch Front</title>
<link rel="stylesheet" href="https://fonts.googleapis.com/css2?family=Lexend+Giga:wght@300;400;600&family=Lexend+Zetta:wght@300&display=swap">
<style>
  :root {
    --backdrop: #f3c7e5;
    --purple: #7a66a3;
    --purple-light: #9b8bb8;
    --purple-text: #6e5697;
    --pink: #e8b5d9;
    --pink-bright: #f0b2e0;
    --ink: #2e2a4c;
    --white: #ffffff;
    --badge-red: #d4504e;
    --badge-green: #2ea57b;
    --badge-blue: #3aaad6;
  }
  html, body {
    margin: 0;
    width: 1200px;
    height: 896px;
    overflow: hidden;
    background: var(--backdrop);
  }
  .pouch-front {
    position: absolute;
    left: 328px;
    top: 28px;
    width: 544px;
    height: 840px;
    box-shadow: 0 10px 18px rgba(120, 60, 110, 0.18);
  }
  .wordmark {
    font-family: "Lexend Giga", sans-serif;
    font-weight: 300;
    fill: var(--white);
  }
  .tagline {
    font-family: "Lexend Giga", sans-serif;
    font-weight: 300;
    fill: var(--pink-bright);
  }
  .descriptor {
    font-family: "Lexend Giga", sans-serif;
    font-weight: 400;
    fill: var(--purple-text);
  }
  .product-name {
    font-family: "Lexend Zetta", sans-serif;
    font-weight: 300;
    fill: var(--pink);
  }
  .audience {
    font-family: "Lexend Giga", sans-serif;
    font-weight: 300;
    fill: var(--purple-text);
  }
  .step-label {
    font-family: "Lexend Giga", sans-serif;
    font-weight: 300;
    fill: var(--ink);
  }
  .seal-label {
    font-family: "Lexend Giga", sans-serif;
    font-weight: 600;
    fill: var(--white);
    text-anchor: middle;
  }
  .sparkle { fill: none; stroke: var(--ink); stroke-width: 1.4; stroke-linejoin: round; }
  .sparkle-light { fill: none; stroke: var(--white); stroke-width: 1.4; stroke-linejoin: round; }
</style>
</head>
<body>
<svg class="pouch-front" viewBox="0 0 544 840" xmlns="http://www.w3.org/2000/svg">
  <defs>
    <linearGradient id="petPhotoTone" x1="0" y1="0" x2="1" y2="1">
      <stop offset="0" stop-color="#e3c28f"/>
      <stop offset="0.55" stop-color="#c89a62"/>
      <stop offset="1" stop-color="#7d6a55"/>
    </linearGradient>
    <linearGradient id="confettiTone" x1="0" y1="0" x2="1" y2="1">
      <stop offset="0" stop-color="#f3d3ea" stop-opacity="0"/>
      <stop offset="1" stop-color="#eec2df" stop-opacity="0.7"/>
    </linearGradient>
    <path id="sparkleShape" d="M0,-10 C1,-2 2,-1 10,0 C2,1 1,2 0,10 C-1,2 -2,1 -10,0 C-2,-1 -1,-2 0,-10 Z"/>
  </defs>

  <rect class="panel-base" width="544" height="840" fill="var(--white)"/>

  <path class="header-wave" fill="var(--purple)"
        d="M0,0 H544 V375 C515,380 490,392 465,394 C430,397 405,398 385,412 C360,432 345,442 320,441 C290,440 275,422 245,420 H0 Z"/>
  <path class="header-blob-left" fill="var(--purple-light)"
        d="M0,0 H297 C270,40 240,70 195,84 C150,98 110,60 70,72 C35,82 15,100 0,110 Z"/>
  <path class="header-blob-right" fill="var(--purple-light)"
        d="M485,0 H544 V322 C520,300 505,260 510,215 C515,170 530,140 520,100 C512,60 500,30 485,0 Z"/>

  <rect class="pet-photo" role="img" aria-label="Photo of a smiling golden retriever beside a tabby cat"
        x="42" y="214" width="150" height="209" rx="40" fill="url(#petPhotoTone)"/>
  <rect class="pet-photo-cat" role="img" aria-label="Photo of a tabby cat beside the dog"
        x="180" y="296" width="122" height="127" rx="30" fill="#8d7a63"/>

  <text class="wordmark" x="200" y="262" font-size="50" textLength="285" lengthAdjust="spacingAndGlyphs">VELUTRA</text>
  <use href="#sparkleShape" class="sparkle-light" transform="translate(471,290) scale(0.8)"/>
  <text class="tagline" x="306" y="333" font-size="21" textLength="177" lengthAdjust="spacingAndGlyphs">Fragrance-Free</text>
  <use href="#sparkleShape" class="sparkle-light" transform="translate(358,364) scale(0.8)"/>

  <use href="#sparkleShape" class="sparkle" transform="translate(189,461) scale(0.8)"/>
  <text class="descriptor" x="106" y="516" font-size="37" textLength="330" lengthAdjust="spacingAndGlyphs">Mineral Instant</text>
  <use href="#sparkleShape" class="sparkle" transform="translate(467,513) scale(1.2)"/>
  <text class="product-name" x="91" y="583" font-size="62" textLength="364" lengthAdjust="spacingAndGlyphs">Absorber</text>
  <line class="rule" x1="115" y1="597" x2="430" y2="597" stroke="var(--ink)" stroke-width="0.8"/>
  <use href="#sparkleShape" class="sparkle" transform="translate(92,633) scale(1.5)"/>
  <text class="audience" x="154" y="640" font-size="22" textLength="234" lengthAdjust="spacingAndGlyphs">For Dogs &amp; Cats</text>

  <g class="step step-sprinkle">
    <rect x="64" y="672" width="123" height="34" fill="var(--white)" stroke="var(--pink)" stroke-width="1"/>
    <path d="M76,682 l10,-3 3,7 -10,3 z M80,690 v2 M84,692 v3 M78,695 v2" stroke="var(--pink)" stroke-width="1.6" fill="var(--pink)" stroke-linecap="round"/>
    <text class="step-label" x="100" y="695" font-size="15" textLength="71" lengthAdjust="spacingAndGlyphs">Sprinkle</text>
  </g>
  <g class="step step-wait">
    <rect x="196" y="672" width="151" height="34" fill="var(--white)" stroke="var(--purple-text)" stroke-width="1"/>
    <circle cx="214" cy="689" r="7" fill="var(--purple-text)"/>
    <path d="M214,684 v5 h3" stroke="var(--white)" stroke-width="1.4" fill="none" stroke-linecap="round"/>
    <text class="step-label" x="227" y="695" font-size="15" textLength="111" lengthAdjust="spacingAndGlyphs">Wait 1–5 min</text>
  </g>
  <g class="step step-sweep">
    <rect x="358" y="672" width="123" height="34" fill="var(--white)" stroke="var(--pink)" stroke-width="1"/>
    <path d="M384,680 l-8,10 M371,691 l5,-2 4,4 -4,4 -6,0 z" stroke="var(--pink)" stroke-width="1.6" fill="var(--pink)" stroke-linecap="round"/>
    <text class="step-label" x="400" y="695" font-size="15" textLength="64" lengthAdjust="spacingAndGlyphs">Sweep</text>
  </g>

  <use href="#sparkleShape" class="sparkle" transform="translate(309,727) scale(0.8)"/>

  <g class="benefit-seals">
    <g class="seal seal-odor">
      <circle cx="196" cy="767" r="29" fill="var(--badge-red)"/>
      <circle cx="196" cy="767" r="24" fill="none" stroke="var(--white)" stroke-width="1.2"/>
      <text class="seal-label" x="196" y="765" font-size="7.5" textLength="30" lengthAdjust="spacingAndGlyphs">ODOR-</text>
      <text class="seal-label" x="196" y="775" font-size="7.5" textLength="38" lengthAdjust="spacingAndGlyphs">BINDING</text>
    </g>
    <g class="seal seal-mineral">
      <circle cx="271" cy="767" r="29" fill="var(--badge-green)"/>
      <circle cx="271" cy="767" r="24" fill="none" stroke="var(--white)" stroke-width="1.2"/>
      <text class="seal-label" x="271" y="765" font-size="8" textLength="26" lengthAdjust="spacingAndGlyphs">100%</text>
      <text class="seal-label" x="271" y="775" font-size="7.5" textLength="38" lengthAdjust="spacingAndGlyphs">MINERAL</text>
    </g>
    <g class="seal seal-dust">
      <circle cx="344" cy="766" r="29" fill="var(--badge-blue)"/>
      <circle cx="344" cy="766" r="24" fill="none" stroke="var(--white)" stroke-width="1.2"/>
      <text class="seal-label" x="344" y="760" font-size="7.5" textLength="38" lengthAdjust="spacingAndGlyphs">LOW-DUST</text>
      <text class="seal-label" x="344" y="770" font-size="6.5" textLength="18" lengthAdjust="spacingAndGlyphs">ECO</text>
      <text class="seal-label" x="344" y="779" font-size="6.5" textLength="36" lengthAdjust="spacingAndGlyphs">FRIENDLY</text>
    </g>
  </g>

  <rect class="confetti-decor" role="img" aria-label="Scattered pink dash confetti decoration"
        x="400" y="730" width="144" height="95" fill="url(#confettiTone)"/>
</svg>
</body>
</html>
```